Music Festival in Colorado Needs Awesome Flier Design

We need an eye-catching & captivating flier design for an annual music festival in Denver, CO (USA). The festival features the best Colorado musicians within the genres of jam - funk - bluegrass - electronic - reggae - rock.

The design should look clean and professional while still being creative and unique. The past three years' flier designs are attached, as well as the logo and some other designs that match the aesthetic of what we're looking for.

This festival has a big element of Colorado pride so any

Target Market(s)

Hippies - live music enthusiasts - partiers. Ages 21 - 40.

Industry/Entity Type

Entertainment

Colors
0355a3
ec1f27
ffffff
fbed22

Requirements
Must have
• Attached design text.
Nice to have
• - Quality texture and psychedelic elements.
• - Colorado pride elements; color scheme (red, white, blue & yellow), flag, ect.
• - Nature elements are awesome but this is also a downtown festival so keep that in mind.
Should not have
• Cheesy artwork.

```html
<!DOCTYPE html>
<html lang="en">
<head>
<meta charset="utf-8">
<title>Raise the Chorus Music Festival</title>
<link href="https://fonts.googleapis.com/css2?family=Lato:wght@400;700;900&family=Big+Shoulders+Display:wght@700;800&display=swap" rel="stylesheet">
<style>
  :root {
    --page: #dcdcdc;
    --sky-top: #2aa9dc;
    --sky-mid: #34c0ec;
    --sky-low: #2fb3e4;
    --navy: #0d2a6b;
    --white: #ffffff;
    --ink: #4a4a4a;
    --forest: #1f4a2a;
    --ridge: #2e4f86;
  }
  * { margin: 0; padding: 0; box-sizing: border-box; }
  html, body { width: 1200px; height: 1200px; overflow: hidden; background: var(--page); }
  .flyer {
    position: absolute; left: 172px; top: 0; width: 856px; height: 1200px; overflow: hidden;
    background:
      radial-gradient(ellipse at 50% 10%, rgba(255,255,255,0.12), transparent 60%),
      linear-gradient(180deg, var(--sky-top) 0%, var(--sky-mid) 40%, var(--sky-low) 75%);
    font-family: 'Lato', sans-serif; color: var(--white);
  }
  .brand {
    position: absolute; top: 132px; width: 100%; text-align: center; white-space: nowrap;
    font: 900 62px/1 'Lato', sans-serif; letter-spacing: 1px;
  }
  .brand-dot {
    display: inline-block; width: 22px; height: 22px; border-radius: 50%;
    background: var(--white); vertical-align: middle; margin-right: 16px; position: relative; top: -6px;
  }
  .event-name {
    position: absolute; top: 314px; width: 100%; text-align: center; white-space: nowrap;
    font: 700 64px/1 'Lato', sans-serif; letter-spacing: 0.5px;
  }
  .headline { position: absolute; left: 0; width: 856px; overflow: visible; }
  .event-type { top: 396px; height: 124px; }
  .event-type text {
    font: 800 154px 'Big Shoulders Display', sans-serif; fill: var(--navy);
    stroke: #bfe9f8; stroke-width: 2px; paint-order: stroke fill;
  }
  .event-dates { top: 534px; height: 72px; }
  .event-dates text { font: 700 72px 'Big Shoulders Display', sans-serif; fill: var(--white); }
  .lineup {
    position: absolute; top: 621px; left: 50px; width: 760px; height: 87px;
    background: var(--white); color: var(--ink);
    padding: 6px 16px; text-align: center; font: 400 18px/1.32 'Lato', sans-serif;
  }
  .contact { position: absolute; top: 750px; display: flex; gap: 14px; font: 700 24px/33px 'Lato', sans-serif; white-space: nowrap; }
  .contact-web { left: 50px; align-items: center; }
  .contact-venue { left: 465px; top: 752px; }
  .contact-venue address { font-style: normal; margin-top: 4px; }
  .contact-icon { width: 45px; height: 45px; flex: none; }
  .contact-venue .contact-icon { margin-right: 6px; margin-top: 3px; }
  .landscape {
    position: absolute; left: 0; bottom: 0; width: 100%; height: 370px;
    background: linear-gradient(180deg,
      rgba(47,179,228,0) 0%, #3a9fd0 18%, #6e97c0 32%, #cfd8e6 38%,
      var(--ridge) 44%, #2d4a74 54%, #2f5a3a 68%, var(--forest) 84%, #5a5a32 100%);
  }
</style>
</head>
<body>
  <main class="flyer">
    <div class="brand"><span class="brand-dot"></span>RAISE THE CHORUS</div>

    <h1 class="event-name">RAISE THE CHORUS</h1>

    <svg class="headline event-type" viewBox="0 0 856 124" role="heading" aria-level="2" aria-label="Music Festival">
      <text x="53" y="117" textLength="760" lengthAdjust="spacingAndGlyphs">MUSIC FESTIVAL</text>
    </svg>

    <svg class="headline event-dates" viewBox="0 0 856 72" aria-label="May 11th - 13th, 2018 (6th annual)">
      <text x="92" y="62" textLength="664" lengthAdjust="spacingAndGlyphs">MAY 11TH - 13TH, 2018 (6TH ANNUAL)</text>
    </svg>

    <p class="lineup">Owen Marsh Band, Open Sky Orchestra, Split Theory, The Copper Kettles, J-Ray &amp; The Summit, Wapiti, Elements, Granite Ensemble, Cloudspun, Polytones, Kaleido, Bright Echo, Pine Junction, Orbits.</p>

    <div class="contact contact-web">
      <svg class="contact-icon" viewBox="0 0 46 46" aria-hidden="true">
        <circle cx="23" cy="23" r="23" fill="#0d2a6b"/>
        <circle cx="23" cy="23" r="11" fill="none" stroke="#fff" stroke-width="2.5"/>
        <ellipse cx="23" cy="23" rx="5" ry="11" fill="none" stroke="#fff" stroke-width="2"/>
        <line x1="12" y1="23" x2="34" y2="23" stroke="#fff" stroke-width="2"/>
      </svg>
      <span>www.raisethechorusfest.com</span>
    </div>

    <div class="contact contact-venue">
      <svg class="contact-icon" viewBox="0 0 46 46" aria-hidden="true">
        <circle cx="23" cy="23" r="23" fill="#0d2a6b"/>
        <path d="M23 10c-5.5 0-9 4-9 8.8 0 6.5 9 17.2 9 17.2s9-10.7 9-17.2C32 14 28.5 10 23 10z" fill="#2fb3e4"/>
        <circle cx="23" cy="19" r="3.5" fill="#0d2a6b"/>
      </svg>
      <address>412 W. Elm Ave Denver,<br>CO 80211</address>
    </div>

    <div class="landscape" role="img" aria-label="Photograph of snow-capped Colorado mountains under a blue sky, with green forested hills and a meadow in front"></div>
  </main>
</body>
</html>
```